The Velvet Needle Poster for a shop Facade

Hello Designers,

• We have a 4X4 meters façade for our tailor shop “The Velvet Needle”, and we are looking for a unique, simple and attractive poster to be printed on the glass to attract the attention of the driving customers or whoever passes by the shop.
• The Velvet Needle, with ‘Velvet’ referring to door-to-door service, our concept as follows (Call … Measure … Stitch … Deliver)

1. Step1: Book online or simply call us to make your appointment (should be pictorial not writing)
2. Step2: Our dedicated personnel will come to you at your preferred time and location. (should be pictorial not writing)
3. Step3: Clothes Alteration/Making to suit your style and body fit. (should be pictorial not writing)
4. Step4: Delivery on completion, at your preferred time and location. (should be pictorial not writing)

• We are specialized in clothes alteration and making for both men and women, and anything related to tailoring services www.thevelvetneedle.example

• The poster must include the name “The Velvet Needle” as well as the phone number 04 318 2976 in a very clear and obvious way (logo will be optional if you can show it in a nice way)
And the concept of our shop should be shown in the poster in a very simple and clear way and more graphical than words. (Perhaps a graphical flow to show client booking our service and we go to their place for alterations done).
Colors should be chosen carefully to attract the customers and the walk-ins eyes when they pass by either walking or by cars.

Thank you
Omar

Target Market(s)

We have a 4X4 meters façade for our tailor shop “The Velvet Needle”, and we are looking for a unique, simple and attractive poster to be printed on the glass to attract the attention of the driving customers or whoever passes by the shop.

Industry/Entity Type

Fashion

• to match the poster/signage

Colors

Designer to choose colors to be used in the design.

Requirements
Must have
Nice to have
• the concept of our shop should be shown in the poster in a very simple and clear way and more graphical than words. (Perhaps a graphical flow to show client booking our service and we go to their place for alterations done).
Should not have
• many words, copied designs. Please only use the images attached in the project brief for reference.

```html
<!DOCTYPE html>
<html lang="en">
<head>
<meta charset="utf-8">
<title>The Velvet Needle – Facade Poster</title>
<link rel="stylesheet" href="https://fonts.googleapis.com/css2?family=Fira+Sans+Condensed:wght@300;600&display=swap">
<style>
  :root {
    --sand: #cfc08f;
    --fabric-dark: #3b2d22;
    --fabric-mid: #5e4633;
    --fabric-warm: #7b4f2f;
    --frame-tan: #8b7650;
    --panel-brown: #54463a;
    --logo-black: #050505;
    --ink-white: #ffffff;
    --ink-black: #0a0806;
    --form-dark: #1a140e;
    --form-shadow: #8a7448;
    --step-fill: #cfc08f;
    --step-ink: #2a2018;
  }
  * { margin: 0; padding: 0; box-sizing: border-box; }
  html, body {
    width: 1200px;
    height: 1162px;
    overflow: hidden;
    background: var(--sand);
  }
  .poster {
    position: relative;
    width: 1200px;
    height: 1162px;
    background: var(--sand);
    font-family: "Fira Sans Condensed", sans-serif;
  }
  .fabric-photo {
    position: absolute;
    inset: 0;
    background: linear-gradient(100deg, var(--fabric-dark) 35%, var(--fabric-mid) 60%, var(--fabric-dark) 72%, var(--fabric-warm) 80%, var(--fabric-warm) 100%);
    clip-path: polygon(423px 0, 1200px 0, 1200px 1162px, 551px 1162px);
  }
  .dress-form {
    position: absolute;
    left: 98px;
    top: 283px;
    width: 282px;
    height: 742px;
    background: linear-gradient(110deg, var(--form-shadow) 0%, var(--form-dark) 45%, var(--form-dark) 100%);
  }
  .call-frame {
    position: absolute;
    left: 304px;
    top: 293px;
    width: 733px;
    height: 507px;
    background: var(--frame-tan);
  }
  .call-panel {
    position: absolute;
    left: 18px;
    top: 17px;
    width: 695px;
    height: 471px;
    background: var(--panel-brown);
  }
  .call-text {
    position: absolute;
    left: 40px;
    top: 40px;
    width: 420px;
    text-align: center;
    font-weight: 600;
    font-size: 66px;
    line-height: 103px;
    color: var(--ink-white);
  }
  .call-phone {
    position: absolute;
    left: 40px;
    top: 350px;
    width: 420px;
    text-align: center;
    font-weight: 600;
    font-size: 66px;
    letter-spacing: 1px;
    color: var(--ink-black);
  }
  .brand-block {
    position: absolute;
    left: 457px;
    top: 30px;
    width: 205px;
    height: 408px;
    background: var(--logo-black);
    display: flex;
    align-items: center;
    justify-content: center;
  }
  .brand-name {
    font-weight: 300;
    font-size: 40px;
    line-height: 48px;
    text-align: center;
    color: var(--ink-white);
  }
  .service-flow {
    position: absolute;
    left: 575px;
    top: 880px;
    width: 560px;
    height: 120px;
  }
</style>
</head>
<body>
  <main class="poster">
    <div class="fabric-photo" role="img" aria-label="Photograph of draped brown and bronze patterned tailoring fabrics"></div>
    <div class="dress-form" role="img" aria-label="Illustration of a black tailor's dress form wrapped in a measuring tape, with a soft shadow"></div>
    <section class="call-frame">
      <div class="call-panel">
        <p class="call-text">Simply call us<br>to make your<br>appointment</p>
        <p class="call-phone">04 318 2976</p>
        <div class="brand-block">
          <p class="brand-name">The Velvet<br>Needle</p>
        </div>
      </div>
    </section>
    <svg class="service-flow" viewBox="0 0 560 120" role="img" aria-label="Service steps: call, we come to you, stitch, deliver">
      <g fill="var(--step-fill)">
        <circle cx="55" cy="60" r="50"/>
        <circle cx="205" cy="60" r="50"/>
        <circle cx="355" cy="60" r="50"/>
        <circle cx="505" cy="60" r="50"/>
      </g>
      <g fill="none" stroke="var(--step-fill)" stroke-width="5" stroke-linecap="round" stroke-linejoin="round">
        <path d="M112 60 H146 M136 50 L147 60 L136 70"/>
        <path d="M262 60 H296 M286 50 L297 60 L286 70"/>
        <path d="M412 60 H446 M436 50 L447 60 L436 70"/>
      </g>
      <path class="icon-phone" fill="var(--step-ink)" d="M38 36 q6 -4 10 2 l6 10 q2 5 -3 8 l-4 3 q4 10 14 16 l3 -4 q3 -5 8 -2 l10 6 q5 4 1 10 l-4 5 q-6 6 -16 1 q-22 -12 -32 -34 q-4 -10 3 -15 z"/>
      <g class="icon-pin">
        <path fill="var(--step-ink)" d="M205 92 q-24 -28 -24 -44 a24 24 0 0 1 48 0 q0 16 -24 44 z"/>
        <circle cx="205" cy="47" r="9" fill="var(--step-fill)"/>
      </g>
      <g class="icon-scissors" fill="none" stroke="var(--step-ink)" stroke-width="5" stroke-linecap="round">
        <circle cx="340" cy="80" r="9"/>
        <circle cx="370" cy="80" r="9"/>
        <path d="M346 73 L376 35 M364 73 L334 35"/>
      </g>
      <path class="icon-tick" fill="none" stroke="var(--step-ink)" stroke-width="9" stroke-linecap="round" stroke-linejoin="round" d="M483 62 L499 78 L528 44"/>
    </svg>
  </main>
</body>
</html>
```